Telmoro Business Card

I already have the conplay logo. I need to develop a professional business card layout

Target Market(s)

Business

Industry/Entity Type

Business

Contact Information for Business Card

Company Name: Telmoro Limited

Font styles to use
Sans Serif

Colors

Designer to choose colors to be used in the design.

Requirements
Must have
• Use current logo
• Need two card size options:
• Small Card: 70mm x 28mm (Landscape)
• Square Card: 65mm x 65mm
Nice to have
• I will need 8-10 files for each name, number and email address (details to follow)

```html
<!DOCTYPE html>
<html lang="en">
<head>
<meta charset="utf-8">
<title>Telmoro Business Cards</title>
<link rel="stylesheet" href="https://fonts.googleapis.com/css2?family=Roboto:wght@400;700;900&display=swap">
<style>
  :root {
    --backdrop: #121314;
    --card: #ffffff;
    --brand-green: #8dc21f;
    --accent-orange: #f0a020;
    --ink: #222222;
    --ink-soft: #444444;
  }
  * { margin: 0; padding: 0; box-sizing: border-box; }
  html, body {
    width: 1200px; height: 880px; overflow: hidden;
    background: var(--backdrop);
    font-family: "Roboto", Arial, sans-serif;
  }
  .stage { position: relative; width: 1200px; height: 880px; }
  .card {
    position: absolute; background: var(--card); overflow: hidden;
    border: 1px solid #d9d9d9;
  }
  .card--small { left: 210px; top: 358px; width: 371px; height: 148px; }
  .card--square { left: 684px; top: 249px; width: 345px; height: 345px; }

  .hero-name {
    position: absolute; color: var(--brand-green); font-weight: 900;
    line-height: 0.86; letter-spacing: -1px;
  }
  .card--small .hero-name { left: 2px; top: 10px; font-size: 62px; }
  .card--square .hero-name { left: 4px; top: 16px; font-size: 112px; }

  .wordmark { position: absolute; display: flex; align-items: flex-end; gap: 4px; }
  .wordmark__name { color: var(--brand-green); font-weight: 900; letter-spacing: 0.5px; line-height: 1; }
  .wordmark__suffix { color: var(--ink-soft); font-weight: 400; line-height: 1; }
  .card--small .wordmark { left: 251px; top: 19px; flex-direction: column; align-items: flex-end; gap: 2px; }
  .card--small .wordmark__name { font-size: 19px; }
  .card--small .wordmark__suffix { font-size: 7px; margin-right: 8px; }
  .card--square .wordmark { left: 18px; top: 293px; }
  .card--square .wordmark__name { font-size: 27px; }
  .card--square .wordmark__suffix { font-size: 10px; padding-bottom: 2px; }

  .contact { position: absolute; color: var(--ink); }
  .contact__name { font-weight: 400; line-height: 1.1; }
  .contact__role { color: var(--ink-soft); line-height: 1.2; }
  .contact__rule { border: 0; border-top: 1px solid var(--accent-orange); }
  .contact__line { display: flex; align-items: center; gap: 3px; line-height: 1.25; }
  .contact__icon { flex: none; }

  .card--small .contact { left: 261px; top: 90px; width: 103px; }
  .card--small .contact__name { font-size: 10px; margin-left: 10px; }
  .card--small .contact__role { font-size: 7px; margin-left: 10px; }
  .card--small .contact__rule { margin: 3px 0 3px 10px; }
  .card--small .contact__line { font-size: 9.5px; }

  .card--square .contact { left: 205px; top: 265px; width: 125px; }
  .card--square .contact__name { font-size: 13px; margin-left: 11px; }
  .card--square .contact__role { font-size: 9.5px; margin-left: 11px; }
  .card--square .contact__rule { margin: 5px 0 4px 11px; }
  .card--square .contact__line { font-size: 12px; }
</style>
</head>
<body>
<main class="stage">

  <section class="card card--small" aria-label="Small business card">
    <div class="hero-name">TEL<br>MORO</div>
    <div class="wordmark">
      <span class="wordmark__name">TELMORO</span>
      <span class="wordmark__suffix">Limited</span>
    </div>
    <div class="contact">
      <p class="contact__name">Arun Desai</p>
      <p class="contact__role">Fashion Designer</p>
      <hr class="contact__rule">
      <p class="contact__line">
        <svg class="contact__icon" width="7" height="6" viewBox="0 0 7 6"><rect x="0.5" y="0.5" width="6" height="5" fill="none" stroke="#f0a020" stroke-width="0.8"/><path d="M0.5 0.8 3.5 3.3 6.5 0.8" fill="none" stroke="#f0a020" stroke-width="0.8"/></svg>
        hi@arundesai.com
      </p>
      <p class="contact__line">
        <svg class="contact__icon" width="7" height="7" viewBox="0 0 7 7"><path d="M1.5 0.5 2.8 2 2 3a4 4 0 0 0 2 2l1-0.8 1.5 1.3-0.8 1A5.5 5.5 0 0 1 0.5 1.3Z" fill="#f0a020"/></svg>
        301 555 0192
      </p>
    </div>
  </section>

  <section class="card card--square" aria-label="Square business card">
    <div class="hero-name">TEL<br>MORO</div>
    <div class="wordmark">
      <span class="wordmark__name">TELMORO</span>
      <span class="wordmark__suffix">Limited</span>
    </div>
    <div class="contact">
      <p class="contact__name">Arun Desai</p>
      <p class="contact__role">Fashion Designer</p>
      <hr class="contact__rule">
      <p class="contact__line">
        <svg class="contact__icon" width="8" height="7" viewBox="0 0 7 6"><rect x="0.5" y="0.5" width="6" height="5" fill="none" stroke="#f0a020" stroke-width="0.8"/><path d="M0.5 0.8 3.5 3.3 6.5 0.8" fill="none" stroke="#f0a020" stroke-width="0.8"/></svg>
        hi@arundesai.com
      </p>
      <p class="contact__line">
        <svg class="contact__icon" width="8" height="8" viewBox="0 0 7 7"><path d="M1.5 0.5 2.8 2 2 3a4 4 0 0 0 2 2l1-0.8 1.5 1.3-0.8 1A5.5 5.5 0 0 1 0.5 1.3Z" fill="#f0a020"/></svg>
        301 555 0192
      </p>
    </div>
  </section>

</main>
</body>
</html>
```